Business Card & Logo Design - Hedge Fund

We need a business card and logo design for a hedge fund. The hedge fund is named Morvane Holdings LLC. Morvane Holdings was created by finance professors and the strategy is based academic research that looks for patterns in stock prices. The design should look conservative, solid, strong. We favor a classic style - nothing flashy. The logo can relate to the name Morvane Holdings, or it could involve a symbol design that connotes "science" . We are open to ideas. We do not want alot of colors - but if any, color - blue is preferred. The font that seems to look best for the name (Morvane Holdings) is arial black. We are open to ideas. Most important - we want to see a mock up of an actual business card with the logo concept embedded. The business card should include space for : company name, individual name, position title, cell phone, address. We hope to have this work done by Sept. 8.

Target Market(s)

We will be meeting with and giving the business card to institutions and high net worth individuals.

Industry/Entity Type

Investment Advisory

Contact Information for Business Card

Company name - Morvane Holdings LLC
Individual name - Peter Vosk
Title - Portfolio Manager
Cell - (482) 555-0137
Address - 2750 Birchwell Lane, Suite 300, Atlanta GA 30327

Font styles to use
Other font styles liked:
• Arial

Colors
3277b5
0255a3
85acd3
cedeed
fdf9cf
d9d9d9
e6e6e6
f04a50
6b449b

Requirements
Must have
• Must have card details that are sited above.
• We would like a logo related to the name (Morvane Holdings) or concept of the fund.
Nice to have
• We want conservative / understated / clean crisp look.
• If any colors - we prefer conservative appearance - blue / gray.
• I have enclosed an example of a card style that looks attractive - please do not exactly copy this card. This is not our company or logo. I feel the layout is attractive - just as an example
Should not have
• Avoid too much color.
• I have selected some preferred colors. Please do not use all of the colors - I have selected a few that might work - but I am not sure. We are open to your ideas so please do not feel the need to use all or any of these.

```html
<!DOCTYPE html>
<html lang="en">
<head>
<meta charset="utf-8">
<title>Morvane Holdings – Business Card</title>
<link href="https://fonts.googleapis.com/css2?family=Source+Sans+3:wght@400;600&display=swap" rel="stylesheet">
<style>
  :root {
    --teal: #045a78;
    --mark-grey: #c4c6c8;
    --text-grey: #58595b;
    --white: #ffffff;
    --frame: #4d4d4d;
  }
  * { margin: 0; padding: 0; box-sizing: border-box; }
  html, body {
    width: 1200px; height: 1132px; overflow: hidden;
    background: var(--white);
    font-family: "Source Sans 3", "Myriad Pro", Arial, sans-serif;
  }
  .sheet { position: relative; width: 1200px; height: 1132px; }

  .card { position: absolute; left: 0; width: 1200px; overflow: hidden; }
  .card-front { top: 0; height: 556px; background: var(--teal); }
  .card-back {
    top: 574px; height: 558px; background: var(--white);
    border: 1.5px solid var(--frame);
  }

  .brand-square { position: absolute; }
  .card-front .brand-square {
    left: 190px; top: 160px; width: 220px; height: 220px; background: var(--mark-grey);
  }
  .card-back .brand-square {
    left: 196px; top: 214px; width: 118px; height: 118px; background: var(--teal);
  }

  .brand-name-large {
    position: absolute; left: 451px; top: 244px;
    font-size: 62px; font-weight: 600; line-height: 1;
    color: var(--white); white-space: nowrap;
  }
  .brand-rule {
    position: absolute; left: 474px; top: 322px; width: 444px; height: 4px;
    background: var(--white);
  }

  .brand-name-small {
    position: absolute; left: 341px; top: 272px;
    font-size: 27px; font-weight: 600; line-height: 1;
    color: var(--text-grey); white-space: nowrap;
  }

  .contact {
    position: absolute; left: 772px; top: 168px;
    color: var(--text-grey); line-height: 1;
  }
  .contact .company { font-size: 26px; font-weight: 600; margin-bottom: 10px; }
  .contact .person, .contact .title { font-size: 27px; font-weight: 400; margin-bottom: 10px; }
  .contact .detail { font-size: 21px; font-weight: 400; margin-bottom: 9px; }
</style>
</head>
<body>
<div class="sheet">
  <section class="card card-front">
    <div class="brand-square"></div>
    <div class="brand-name-large">Morvane Holdings</div>
    <div class="brand-rule"></div>
  </section>

  <section class="card card-back">
    <div class="brand-square"></div>
    <div class="brand-name-small">Morvane Holdings</div>
    <div class="contact">
      <p class="company">Morvane Holdings LLC</p>
      <p class="person">Peter Vosk</p>
      <p class="title">Portfolio Manager</p>
      <p class="detail">Cell:(482)555-0137</p>
      <p class="detail">2750 Birchwell Lane</p>
      <p class="detail">Suite 300</p>
      <p class="detail">Atlanta GA 30327</p>
    </div>
  </section>
</div>
</body>
</html>
```